Podcast Cover Art for Fast Growing Show (Ill include a gracious tip!)

This artwork is for "The Steadfast Fellow Show." The podcast is for men, and it's all about self-improvement, confidence, success, money, women and masculinity. It's for the guy who wants to improve himself. I'd like for my picture to be included — in black and white — and I want the text to read: "The Steadfast Fellow Show" and somewhere in there it'll say: "with Dale Prowen." I'm open to color schemes. The podcast is a little edgy so I'd like for that to be represented in the design. Thank you! (((Here's the podcast page if you wanna check it out: http://steadfastfellowshow.castorbit.net/)))

Target Market(s)

Men who want to attract women and improve their lives!

Font styles to use
Serif

Colors

Designer to choose colors to be used in the design.

Requirements
Must have
• My image in it (in black and white) and the two titles: "The Steadfast Fellow Show" and "with Dale Prowen"
Nice to have
• My logo in it somehow (which is the arrow looking logo attached below). I've also found that my image looks best in black and white and with a circular type cut out (although I'm open to different design ideas). I've attached my logo with a circular cut out below so you can see what I'm talking about.
Should not have
• Flowers. Teddy bears. ice cream.

```html
<!DOCTYPE html>
<html lang="en">
<head>
<meta charset="utf-8">
<title>The Steadfast Fellow Show — Cover Art</title>
<link rel="stylesheet" href="https://fonts.googleapis.com/css2?family=Playfair+Display:wght@700&family=Inter:wght@400&display=swap">
<style>
  :root {
    --bg: #0b0b0b;
    --title-white: #ffffff;
    --accent-red: #e8343a;
    --photo-light: #9a9a9a;
    --photo-mid: #4a4a4a;
    --photo-dark: #141414;
  }
  html, body {
    margin: 0;
    padding: 0;
    width: 1200px;
    height: 1200px;
    overflow: hidden;
    background: var(--bg);
  }
  .cover {
    position: relative;
    width: 1200px;
    height: 1200px;
    background: var(--bg);
    overflow: hidden;
  }
  .cover svg { display: block; }
  .title-line {
    font-family: "Playfair Display", Georgia, serif;
    font-weight: 700;
    fill: var(--title-white);
  }
  .host-credit {
    font-family: "Inter", "Helvetica Neue", Arial, sans-serif;
    font-weight: 400;
    fill: var(--title-white);
  }
</style>
</head>
<body>
  <main class="cover">
    <svg width="1200" height="1200" viewBox="0 0 1200 1200" xmlns="http://www.w3.org/2000/svg">
      <defs>
        <radialGradient id="hostPhotoTone" cx="0.62" cy="0.42" r="0.7">
          <stop offset="0" stop-color="var(--photo-light)"/>
          <stop offset="0.5" stop-color="var(--photo-mid)"/>
          <stop offset="1" stop-color="var(--photo-dark)"/>
        </radialGradient>
      </defs>

      <!-- host portrait area -->
      <path class="host-photo" role="img"
            aria-label="Black and white portrait of host Dale Prowen, hands steepled in front of his face"
            fill="url(#hostPhotoTone)"
            d="M860 60 Q1000 20 1200 40 L1200 1200 L250 1200 Q330 1010 520 940 Q690 880 740 800 Q720 600 740 420 Q760 160 860 60 Z"/>

      <!-- show title -->
      <g class="show-title">
        <text class="title-line title-the" x="38" y="135" font-size="64" textLength="115" lengthAdjust="spacingAndGlyphs">The</text>
        <text class="title-line title-main" x="50" y="300" font-size="160" textLength="1060" lengthAdjust="spacingAndGlyphs">Steadfast</text>
        <text class="title-line title-second" x="50" y="480" font-size="120" textLength="360" lengthAdjust="spacingAndGlyphs">Fellow</text>
        <text class="title-line title-third" x="50" y="650" font-size="140" textLength="470" lengthAdjust="spacingAndGlyphs">Show.</text>
      </g>

      <!-- red underline stroke -->
      <path class="accent-underline" d="M8 353 Q600 300 1145 333" stroke="var(--accent-red)" stroke-width="12" stroke-linecap="round" fill="none"/>

      <!-- host credit -->
      <text class="host-credit" x="45" y="760" font-size="52">with Dale Prowen.</text>
    </svg>
  </main>
</body>
</html>
```